Postcard Design

I am in real estate, I wish to design a "farming" tool.

I want to show a sampling of houses (files attached) with the following text:

The spring market is here and the buyers are waiting for YOU!
Order a Value Glance to see what homes in your neighborhood are selling for, or call today for a personal market analysis.

Order your report at: www.48213HouseDeals.net
or reach out to me directly:
Dana Holloway
www.SettleinBrexham.net
555.214.7860
YourRealtorDana@Maildrop.net

I also attached multiple files containing logos - in multiple formats and in black or white, depending on what is easier to use.

Target Market(s)

By neighborhood. I have a list.

Industry/Entity Type

Real Estate

Requirements
Must have
• See description above

```html
<!DOCTYPE html>
<html lang="en">
<head>
<meta charset="utf-8">
<title>Spring Market Postcard – Dana Holloway</title>
<link rel="stylesheet" href="https://fonts.googleapis.com/css2?family=EB+Garamond:ital,wght@0,400;0,500;0,600;1,400&family=Pinyon+Script&display=swap">
<style>
  :root {
    --brown: #5a3f36;
    --sky: #a9e3f6;
    --tan: #c8bd9e;
    --white: #ffffff;
    --ink: #4f3a32;
    --photo-sky: #c9dbe6;
    --photo-house: #8f8a7c;
    --photo-lawn: #6f8f4e;
  }
  * { box-sizing: border-box; margin: 0; padding: 0; }
  html, body { width: 1200px; height: 1000px; overflow: hidden; background: var(--white); }
  body { position: relative; font-family: "EB Garamond", Georgia, serif; color: var(--ink); }
  .block { position: absolute; }

  /* Back of postcard */
  .card-back { position: absolute; left: 62px; top: 42px; width: 858px; height: 648px;
    border-right: 1px solid #222; border-bottom: 1px solid #222; background: var(--white); }
  .tan { background: var(--tan); }
  .brown { background: var(--brown); }
  .sky { background: var(--sky); }
  .photo { background: linear-gradient(180deg, var(--photo-sky) 0%, #b9c4c6 35%, var(--photo-house) 60%, var(--photo-lawn) 100%); }

  .offer-banner { left: 265px; top: 0; width: 593px; height: 113px; display: flex; align-items: center; justify-content: center; text-align: center;
    color: var(--white); font-style: italic; font-size: 24px; line-height: 1.22; letter-spacing: 0.3px; padding: 0 40px; }

  .brand { display: flex; flex-direction: column; align-items: center; justify-content: center; color: var(--white); font-weight: 400; }
  .brand .name { font-size: 26px; line-height: 1; }
  .brand .firm { font-size: 9px; letter-spacing: 1.6px; margin-top: 5px; }

  .contact { left: 0; top: 393px; width: 248px; height: 255px; padding: 52px 0 0 21px; font-size: 15.5px; line-height: 1.33; }
  .contact .lead { font-style: italic; }
  .contact .detail { font-weight: 600; }
  .contact .gap { height: 19px; }

  /* Front of postcard */
  .card-front { position: absolute; left: 405px; top: 383px; width: 761px; height: 585px; background: var(--white); }
  .logo-frame { left: 262px; top: 17px; width: 241px; height: 150px; background: var(--white); padding: 9px 10px; }
  .logo-frame .brand { width: 100%; height: 100%; background: var(--brown); }
  .logo-frame .brand .name { font-size: 28px; }

  .headline { left: 0; top: 150px; width: 761px; text-align: center; font-size: 45px; line-height: 1.1; color: var(--brown); }
  .headline .line { display: block; }
  .headline .script { font-family: "Pinyon Script", cursive; color: var(--white); font-size: 62px; line-height: 0.8; }
  .headline .l1 { padding-left: 40px; }
  .headline .l2 { padding-left: 120px; }
  .headline .l3 { padding-left: 30px; }
</style>
</head>
<body>

<section class="card-back" aria-label="Postcard back">
  <div class="block tan" style="left:0;top:0;width:60px;height:113px"></div>
  <div class="block photo" role="img" aria-label="Photo of a two-storey suburban house with garage" style="left:71px;top:0;width:177px;height:113px"></div>
  <p class="block brown offer-banner">Order a Value Glance to see what homes in your neighborhood are selling for, or call today for a personal market analysis.</p>

  <div class="block sky brand" style="left:0;top:125px;width:248px;height:126px">
    <span class="name">Dana Holloway</span>
    <span class="firm">BROOKMERE REAL ESTATE</span>
  </div>
  <div class="block brown" style="left:0;top:266px;width:248px;height:112px"></div>

  <div class="block sky contact">
    <p class="lead">Order your report at:</p>
    <p class="detail">www.48213HouseDeals.net</p>
    <div class="gap"></div>
    <p class="lead">or reach out to me directly:</p>
    <p class="detail">Dana Holloway</p>
    <p class="detail">www.SettleinBrexham.net</p>
    <p class="detail">555.214.7860</p>
    <p class="detail">YourRealtorDana@Maildrop.net</p>
  </div>
</section>

<section class="card-front" aria-label="Postcard front">
  <div class="block sky" style="left:0;top:0;width:761px;height:84px"></div>
  <div class="block sky" style="left:0;top:111px;width:761px;height:291px"></div>

  <div class="block logo-frame">
    <div class="brand">
      <span class="name">Dana Holloway</span>
      <span class="firm">BROOKMERE REAL ESTATE</span>
    </div>
  </div>

  <h1 class="block headline" style="font-weight:400">
    <span class="line l1">The spring market is <span class="script">here</span></span>
    <span class="line l2">and buyers are waiting</span>
    <span class="line l3">for <span class="script">You!</span></span>
  </h1>

  <div class="block brown" style="left:0;top:412px;width:73px;height:133px"></div>
  <div class="block photo" role="img" aria-label="Photo of a beige colonial house with lawn" style="left:83px;top:412px;width:185px;height:133px"></div>
  <div class="block photo" role="img" aria-label="Photo of a blue-grey house with bare trees" style="left:279px;top:412px;width:185px;height:133px"></div>
  <div class="block tan" style="left:474px;top:412px;width:59px;height:133px"></div>
  <div class="block photo" role="img" aria-label="Photo of a grey two-storey house with double garage" style="left:542px;top:412px;width:185px;height:133px"></div>
  <div class="block brown" style="left:737px;top:412px;width:24px;height:133px"></div>

  <div class="block sky" style="left:0;top:554px;width:761px;height:31px"></div>
</section>

</body>
</html>
```